Website design for management consulting firm

We need a web design for a new consulting company based in Boston, MA called "Fernhollow Ridge Consulting." This webpage will be simple home page, with a "contact us" page, that describes the services of the consulting firm. The company provides strategic planning, business assessment, process re-designs, and other management consulting functions. I would like the website to look high-tech. A logo was already created via Pixel Harbor.

Target Market(s)

Other business owners across a wide spectrum of industries - from IT to retail.

Industry/Entity Type

It Company

Number of Pages Required

3 page

Colors
0455a3
ffffff

Requirements
Must have
• Front page that provides generic text / overview of the firm. A "services" tab that describes consulting services. A "contact us" tab that provides either a form to contact us or just the contact email address of the company. info@fernhollowridgeconsulting.example

```html
<!DOCTYPE html>
<html lang="en">
<head>
<meta charset="utf-8">
<title>Fernhollow Ridge Consulting</title>
<link href="https://fonts.googleapis.com/css2?family=Lato:wght@400;700&family=Montserrat:wght@600;700&family=Questrial&display=swap" rel="stylesheet">
<style>
:root{
  --teal:#17a898;
  --navy:#0455a3;
  --deep-navy:#0b3f86;
  --heading-blue:#0e6b91;
  --nav-dark:#242424;
  --ink:#1a1a1a;
  --body-text:#6a6a6a;
  --white:#ffffff;
  --footer-top:#454545;
  --footer-bottom:#111111;
}
*{box-sizing:border-box;margin:0;padding:0}
html,body{width:861px;height:1200px;overflow:hidden;background:var(--white)}
body{position:relative;font-family:'Lato',sans-serif;color:var(--ink)}
.abs{position:absolute}

/* header */
.brand{left:66px;top:15px;display:flex;align-items:center;gap:10px}
.brand-square{width:46px;height:50px;background:var(--navy)}
.brand-name{font-family:'Lato',sans-serif;font-weight:700;font-size:21px;color:var(--ink);line-height:1.05;width:180px}
.pill{top:27px;height:27px;border-radius:14px;background:linear-gradient(#f4f4f4,#dcdcdc);border:1px solid #cfcfcf;display:flex;align-items:center;gap:6px;padding:0 8px 0 4px;font-size:10px;font-weight:700;color:var(--ink)}
.pill .ico{width:20px;height:20px;border-radius:50%;background:var(--deep-navy);display:flex;align-items:center;justify-content:center}
.pill-phone{left:482px;width:108px}
.pill-mail{left:610px;width:185px;font-size:8.6px}

/* nav */
.nav{left:0;top:79px;width:861px;height:37px;background:var(--nav-dark)}
.nav a{position:absolute;top:0;height:37px;line-height:37px;color:var(--white);text-decoration:none;font-family:'Montserrat',sans-serif;font-weight:600;font-size:11px;letter-spacing:.3px}
.nav .active{left:66px;width:62px;background:var(--teal);text-align:center}
.search{left:608px;top:8px;width:187px;height:21px;background:var(--white);font-size:9px;color:#444;padding:5px 8px}
.search svg{position:absolute;right:8px;top:5px}

/* hero */
.hero-photo{left:0;top:116px;width:861px;height:328px;background:radial-gradient(ellipse at 72% 50%,#5fc2b8 0 12%,transparent 26%),linear-gradient(160deg,#cfcfcf 0%,#f2f2f2 45%,#e4e4e4 100%)}
.hero-arrow{top:280px}
.hero-title{left:67px;top:326px;font-family:'Montserrat',sans-serif;font-weight:700;font-size:22.5px;color:var(--heading-blue)}
.hero-cta{left:66px;top:367px;width:241px;height:37px;background:var(--teal);color:var(--white);font-family:'Montserrat',sans-serif;font-weight:700;font-size:23px;line-height:37px;text-align:center}

/* about */
.section-title{left:0;width:861px;text-align:center;font-family:'Questrial',sans-serif;font-size:21px;color:#444}
.section-title b{font-family:'Montserrat',sans-serif;font-weight:700;color:var(--ink);font-size:19px}
.about-title{top:470px}
.dash{left:292px;top:500px;width:277px;border-top:1px dashed #bbb}
.about-text{left:82px;top:510px;width:697px;text-align:center;font-size:10px;line-height:16px;color:var(--body-text)}
.read-more{left:0;width:817px;top:589px;text-align:center;font-size:10px;font-weight:700;color:#444;text-decoration:underline}

/* services */
.services{left:0;top:631px;width:861px;height:330px;background:linear-gradient(#f2f2f2,#e2e2e2 70%,#d8d8d8)}
.services-title{top:651px}
.svc-head{font-family:'Montserrat',sans-serif;font-weight:700;font-size:13px;color:var(--ink);letter-spacing:.2px}
.svc-text{font-size:10px;line-height:15px;color:var(--body-text);width:236px}
.left{right:549px;text-align:right}
.right{left:549px}
.circle{width:84px;height:84px;border-radius:50%;display:flex;align-items:center;justify-content:center;border:2px solid rgba(255,255,255,.6)}
.c-navy{background:radial-gradient(circle at 40% 35%,#1f64b8,var(--deep-navy))}
.c-teal{background:radial-gradient(circle at 40% 35%,#30c2b0,#138d80)}

/* footer */
.footer-wave{left:0;top:900px}
.footer{left:0;top:960px;width:861px;height:208px;background:linear-gradient(#3b3b3b,var(--footer-bottom))}
.f-head{top:990px;font-family:'Montserrat',sans-serif;font-weight:600;font-size:11px;color:var(--white);padding-bottom:7px;border-bottom:1px solid #666}
.f-text{font-size:9.5px;color:#e6e6e6;line-height:13px}
.links li{list-style:none;font-size:9.5px;color:#e6e6e6;position:absolute;left:0;white-space:nowrap}
.links li::before{content:"•";margin-right:6px;color:#ccc}
.links .current{color:#4ea6e6;font-weight:700}
.f-label{font-size:9.5px;color:#e6e6e6;text-align:right;width:60px;left:396px}
.f-input{left:467px;width:157px;background:var(--white);border-radius:3px}
.submit{left:467px;top:1110px;width:55px;height:19px;background:var(--teal);border-radius:3px;color:var(--white);font-size:10px;font-weight:700;text-align:center;line-height:19px}
.social-dot{left:692px;width:25px;height:25px;border-radius:50%}
.social-name{left:730px;font-size:10px;color:var(--white);line-height:10px}
.social-name small{display:block;font-size:7px;font-weight:700}
.copyright{left:0;top:1168px;width:861px;height:32px;background:var(--navy);color:var(--white);font-size:8.5px;font-weight:700;text-align:center;line-height:32px}
</style>
</head>
<body>

<header>
  <div class="abs brand">
    <div class="brand-square"></div>
    <div class="brand-name">Fernhollow Ridge Consulting</div>
  </div>
  <div class="abs pill pill-phone"><span class="ico"><svg width="10" height="10" viewBox="0 0 24 24"><path fill="#fff" d="M6.6 10.8a15 15 0 006.6 6.6l2.2-2.2a1 1 0 011-.25 11.4 11.4 0 003.6.57 1 1 0 011 1V20a1 1 0 01-1 1A17 17 0 013 4a1 1 0 011-1h3.5a1 1 0 011 1c0 1.25.2 2.45.57 3.6a1 1 0 01-.25 1z"/></svg></span>+100555-01234</div>
  <div class="abs pill pill-mail"><span class="ico"><svg width="11" height="8" viewBox="0 0 22 16"><rect width="22" height="16" rx="1" fill="#fff"/><path d="M1 1l10 8 10-8" stroke="#0b3f86" stroke-width="2" fill="none"/></svg></span>names@fernhollowridgeconsulting.example</div>
</header>

<nav class="abs nav">
  <a class="active" href="#">HOME</a>
  <a style="left:208px" href="#">ABOUT US</a>
  <a style="left:354px" href="#">SERVICES &#8964;</a>
  <a style="left:507px" href="#">CONTACT US</a>
  <div class="abs search">Search
    <svg width="11" height="11" viewBox="0 0 12 12"><circle cx="5" cy="5" r="3.8" stroke="#999" stroke-width="1.3" fill="none"/><path d="M8 8l3 3" stroke="#999" stroke-width="1.3"/></svg>
  </div>
</nav>

<section>
  <div class="abs hero-photo" role="img" aria-label="Rows of white paper boats with a single teal paper boat leading"></div>
  <svg class="abs hero-arrow" style="left:16px" width="26" height="46" viewBox="0 0 26 46"><path d="M24 2L3 23l21 21" stroke="#8a8a8a" stroke-width="3.5" fill="none"/></svg>
  <svg class="abs hero-arrow" style="left:809px" width="26" height="46" viewBox="0 0 26 46"><path d="M2 2l21 21L2 44" stroke="#8a8a8a" stroke-width="3.5" fill="none"/></svg>
  <h1 class="abs hero-title">Helping With Any of Your Business Needs</h1>
  <div class="abs hero-cta">Get Started With Us</div>
</section>

<section>
  <h2 class="abs section-title about-title">About <b>Fernhollow Ridge Consulting</b></h2>
  <div class="abs dash"></div>
  <p class="abs about-text">Lorem ipsum dolor sit amet, consectetuer adipiscing elit, sed diam nonummy nibh euismod tincidunt ut laoreet dolore magna aliquam erat volutpat. Ut wisi enim ad minim veniam, quis nostrud exerci tation ullamcorper suscipit lobortis nisl ut aliquip ex ea commodo consequat. Duis autem vel eum iriure dolor in hendrerit in vulputate velit esse molestie consequat, vel illum dolore eu feugiat nulla facilisis at vero eros et accumsan et iusto odio dignissim qui blandit praesent luptatum zzril delenit augue duis dolore te feugait nulla facilisi.</p>
  <a class="abs read-more">Read More</a>
</section>

<section>
  <div class="abs services"></div>
  <h2 class="abs section-title services-title">Our <b>Services</b></h2>

  <h3 class="abs svc-head left" style="top:700px">STRATEGIC PLANNING</h3>
  <p class="abs svc-text left" style="top:729px">Lorem ipsum dolor sit amet, consectetuer adipiscing elit, sed diam nonummy nibh euismod tincidunt ut laoreetfgf dolore magna aliquam</p>
  <div class="abs circle c-navy" style="left:332px;top:700px">
    <svg width="40" height="40" viewBox="0 0 40 40"><circle cx="20" cy="20" r="8" fill="none" stroke="#fff" stroke-width="5" stroke-dasharray="4 2.3"/><circle cx="20" cy="20" r="3.5" fill="#fff"/></svg>
  </div>
  <div class="abs circle c-teal" style="left:445px;top:700px">
    <svg width="40" height="40" viewBox="0 0 40 40"><circle cx="23" cy="16" r="10" fill="none" stroke="#fff" stroke-width="3"/><path d="M15 24L6 33" stroke="#fff" stroke-width="4" stroke-linecap="round"/></svg>
  </div>
  <h3 class="abs svc-head right" style="top:701px">BUSINESS ASSESSMENT</h3>
  <p class="abs svc-text right" style="top:729px">Lorem ipsum dolor sit amet, consectetuer adipiscing elit, sed diam nonummy nibh euismod tincidunt ut laoreetfgf dolore magna aliquam erat</p>

  <h3 class="abs svc-head left" style="top:816px">PROCESS RE-DESIGNS</h3>
  <p class="abs svc-text left" style="top:844px">Lorem ipsum dolor sit amet, consectetuer adipiscing elit, sed diam nonummy nibh euismod tincidunt ut laoreetfgf dolore magna aliquam e</p>
  <div class="abs circle c-teal" style="left:332px;top:815px">
    <svg width="42" height="42" viewBox="0 0 42 42"><path d="M8 22a13 13 0 0122-10" stroke="#fff" stroke-width="3" fill="none"/><path d="M31 6v8h-8" stroke="#fff" stroke-width="3" fill="none"/><path d="M34 20a13 13 0 01-22 10" stroke="#fff" stroke-width="3" fill="none"/><path d="M11 36v-8h8" stroke="#fff" stroke-width="3" fill="none"/></svg>
  </div>
  <div class="abs circle c-navy" style="left:445px;top:815px">
    <svg width="40" height="40" viewBox="0 0 40 40"><rect x="9" y="7" width="20" height="27" rx="2" fill="none" stroke="#fff" stroke-width="2.5"/><rect x="15" y="4" width="8" height="5" fill="#fff"/><path d="M13 16h12M13 22h12M13 28h8" stroke="#fff" stroke-width="2"/><path d="M33 10v22" stroke="#fff" stroke-width="3"/></svg>
  </div>
  <h3 class="abs svc-head right" style="top:815px">CONSULTING FUNCTIONS</h3>
  <p class="abs svc-text right" style="top:844px">Lorem ipsum dolor sit amet, consectetuer adipiscing elit, sed diam nonummy nibh euismod tincidunt ut laoreetfgf dolore magna aliquam</p>
</section>

<footer>
  <svg class="abs footer-wave" width="861" height="62" viewBox="0 0 861 62" preserveAspectRatio="none">
    <defs><linearGradient id="waveFill" x1="0" y1="0" x2="0" y2="1"><stop offset="0" stop-color="#444"/><stop offset="1" stop-color="#3b3b3b"/></linearGradient></defs>
    <path d="M0 30C120 0 240 10 380 30S700 60 861 8V62H0z" fill="url(#waveFill)"/>
    <path d="M380 28C520 60 720 56 861 4" stroke="#17a898" stroke-width="5" fill="none"/>
  </svg>
  <div class="abs footer"></div>

  <h4 class="abs f-head" style="left:70px;width:84px">QUICK LINKS</h4>
  <ul class="abs links" style="left:68px;top:1030px">
    <li class="current" style="top:0">Home</li>
    <li style="top:23px">About Us</li>
    <li style="top:45px">Services</li>
    <li style="top:74px">Contact us</li>
  </ul>

  <h4 class="abs f-head" style="left:216px;width:146px">CONTACT INFORMATION</h4>
  <div class="abs f-text" style="left:216px;top:1018px;width:150px"><b>Fernhollow Ridge Consulting</b><br>123, Lorem ipsum dolor si amet, consectetue &nbsp;nibh euismod</div>
  <div class="abs f-text" style="left:216px;top:1073px">&#9742;&nbsp; (555) 010 - 1225</div>
  <div class="abs f-text" style="left:216px;top:1103px">&#9993;&nbsp; info@fernhollowridgeconsulting.example</div>

  <h4 class="abs f-head" style="left:424px;width:205px">QUICK CONTACT</h4>
  <div class="abs f-label" style="top:1027px">Name</div>
  <div class="abs f-input" style="top:1025px;height:16px"></div>
  <div class="abs f-label" style="top:1049px">Email</div>
  <div class="abs f-input" style="top:1046px;height:16px"></div>
  <div class="abs f-label" style="top:1071px">Message</div>
  <div class="abs f-input" style="top:1069px;height:33px"></div>
  <div class="abs submit">SUBMIT</div>

  <h4 class="abs f-head" style="left:692px;width:105px">FOLLOW &nbsp;US</h4>
  <div class="abs social-dot" style="top:1025px;background:#2e4f8f"></div>
  <div class="abs social-name" style="top:1027px">FRIENDLOOP<small>BECOME A FAN</small></div>
  <div class="abs social-dot" style="top:1070px;background:#0d6ea3"></div>
  <div class="abs social-name" style="top:1072px">WORKGRID<small>JOIN US ON</small></div>
  <div class="abs social-dot" style="top:1115px;background:#1b8fd8"></div>
  <div class="abs social-name" style="top:1117px">SPACEROOM<small>JOIN US ON</small></div>

  <div class="abs copyright">© 2015 Fernhollow Ridge Consulting. All Rights Reserved.</div>
</footer>

</body>
</html>
```